Brenlow Development and Management Corp Stationery Design Project

Based on the logo, a stationary format that can be used for correspondence with all project stakeholders. Typically this involves landowners, public officials, general public, and investors. It needs to be clean and professional, representing the two engineers that manage the company.
Updates

Reason: Logo design finalized. Project updated for revisitation. Thanks,

Target Market(s)

Public officials, investors, project stakeholders, and landowners. All or english speaking, residing in North America. Company is based in Calgary, Alberta, Canada. Project values range fro $10MM to $500MM CAD.

Industry/Entity Type

It Company

Requirements
Should not have
• No references to tropics, palm trees, or similar beaches.

```html
<!DOCTYPE html>
<html lang="en">
<head>
<meta charset="utf-8">
<title>Brenlow Development and Management Corp — Stationery</title>
<link rel="stylesheet" href="https://fonts.googleapis.com/css2?family=Lato:wght@400;700&display=swap">
<style>
  :root {
    --lime: #a2e01c;
    --ink: #1b2129;
    --ink-line: #2b323b;
    --paper: #ffffff;
    --stone: #7f878e;
    --stone-light: #a5acb2;
    --rule: #d6dadd;
    --pale-lime: #eaf5d2;
    --type: "Lato", Arial, sans-serif;
  }
  * { box-sizing: border-box; margin: 0; padding: 0; }
  html, body { width: 1200px; height: 513px; overflow: hidden; background: var(--paper); }
  body { position: relative; font-family: var(--type); }

  .piece { position: absolute; overflow: hidden; }
  .piece--light { background: var(--paper); border: 1px solid var(--rule); }
  .piece--dark { background: var(--ink); }

  .brand { position: absolute; display: flex; flex-direction: column; }
  .brand__row { display: flex; align-items: center; }
  .brand__square { background: var(--stone); flex: none; }
  .brand__name { color: var(--lime); font-weight: 700; letter-spacing: 0.04em; line-height: 1; }
  .brand__tagline { color: var(--stone); font-weight: 400; line-height: 1.2; white-space: nowrap; }
  .piece--dark .brand__tagline { color: var(--stone-light); }

  .contact { position: absolute; color: var(--stone); line-height: 1.45; white-space: nowrap; }
  .piece--dark .contact { color: #5d656d; }

  .flap {
    position: absolute; left: 0; top: 0; width: 100%;
    background: var(--lime);
    border-radius: 0 0 14px 14px;
    color: var(--paper); text-align: center;
  }

  /* business card, light */
  .card-light { left: 124px; top: 163px; width: 113px; height: 65px; }
  /* envelope, light */
  .envelope-light { left: 56px; top: 253px; width: 183px; height: 98px; }
  /* letterhead */
  .letterhead { left: 279px; top: 76px; width: 267px; height: 380px; }
  .letterhead__bar { position: absolute; left: 0; top: 0; width: 100%; height: 6px; background: var(--ink); }
  .letterhead__ground { position: absolute; left: 50px; top: 342px; width: 216px; height: 6px; background: var(--pale-lime); }
  .letterhead__footer {
    position: absolute; left: 50px; top: 359px;
    display: flex; gap: 12px; align-items: center;
    font-size: 4.5px; color: var(--stone); white-space: nowrap;
  }
  .letterhead__footer span + span::before { content: "•"; margin-right: 5px; }
  /* folder */
  .folder { left: 643px; top: 78px; width: 266px; height: 378px; }
  .folder__bar { position: absolute; left: 0; top: 0; width: 100%; height: 7px; background: var(--lime); }
  /* business card, dark */
  .card-dark { left: 950px; top: 160px; width: 114px; height: 64px; }
  /* envelope, dark */
  .envelope-dark { left: 948px; top: 250px; width: 183px; height: 96px; }
</style>
</head>
<body>

  <!-- Business card, light -->
  <section class="piece piece--light card-light">
    <div class="brand" style="left:6px; top:14px;">
      <div class="brand__row" style="gap:3px;">
        <span class="brand__square" style="width:7px; height:7px;"></span>
        <span class="brand__name" style="font-size:9px;">BRENLOW</span>
      </div>
      <span class="brand__tagline" style="font-size:3.2px; margin-top:2px;">Development and Management Corp</span>
    </div>
    <p class="contact" style="left:6px; top:44px; font-size:3.6px;">123 Main Street, Any City, US 12345<br>+1 555 555 5555<br>email@company.com</p>
  </section>

  <!-- Envelope, light -->
  <section class="piece piece--light envelope-light">
    <div class="flap" style="height:32px; padding-top:9px; font-size:4px; line-height:1.45;">
      123 Main Street, Any City, US 12345<br>+1 555 555 5555<br>email@company.com
    </div>
    <div class="brand" style="left:5px; top:74px;">
      <div class="brand__row" style="gap:3px;">
        <span class="brand__square" style="width:8px; height:8px;"></span>
        <span class="brand__name" style="font-size:10px;">BRENLOW</span>
      </div>
      <span class="brand__tagline" style="font-size:3.4px; margin-top:2px;">Development and Management Corp</span>
    </div>
  </section>

  <!-- Letterhead -->
  <section class="piece piece--light letterhead">
    <div class="letterhead__bar"></div>
    <div class="brand" style="left:13px; top:52px;">
      <div class="brand__row" style="gap:5px;">
        <span class="brand__square" style="width:14px; height:14px;"></span>
        <span class="brand__name" style="font-size:17px;">BRENLOW</span>
      </div>
      <span class="brand__tagline" style="font-size:5.2px; margin-top:4px;">Development and Management Corp</span>
    </div>
    <div class="letterhead__ground"></div>
    <p class="letterhead__footer">
      <span>123 Main Street, Any City, US 12345</span>
      <span>+1 555 555 5555</span>
      <span>email@company.com</span>
    </p>
  </section>

  <!-- Presentation folder -->
  <section class="piece piece--dark folder">
    <div class="folder__bar"></div>
    <div class="brand" style="left:60px; top:140px;">
      <div class="brand__row" style="gap:7px;">
        <span class="brand__square" style="width:22px; height:22px;"></span>
        <span class="brand__name" style="font-size:26px;">BRENLOW</span>
      </div>
      <span class="brand__tagline" style="font-size:6.6px; margin-top:5px; margin-left:29px;">Development and Management Corp</span>
    </div>
    <p class="contact" style="left:27px; top:333px; font-size:5.6px;">123 Main Street, Any City, US 12345<br>+1 555 555 5555<br>email@company.com</p>
  </section>

  <!-- Business card, dark -->
  <section class="piece piece--dark card-dark">
    <div class="brand" style="left:25px; top:12px;">
      <div class="brand__row" style="gap:3px;">
        <span class="brand__square" style="width:8px; height:8px;"></span>
        <span class="brand__name" style="font-size:10px;">BRENLOW</span>
      </div>
      <span class="brand__tagline" style="font-size:3.2px; margin-top:2px; margin-left:11px;">Development and Management Corp</span>
    </div>
    <p class="contact" style="left:40px; top:42px; font-size:3.6px;">123 Main Street, Any City, US 12345<br>+1 555 555 5555<br>email@company.com</p>
  </section>

  <!-- Envelope, dark -->
  <section class="piece piece--dark envelope-dark">
    <div class="flap" style="height:26px;"></div>
    <div class="brand" style="left:57px; top:38px;">
      <div class="brand__row" style="gap:3px;">
        <span class="brand__square" style="width:9px; height:9px;"></span>
        <span class="brand__name" style="font-size:11px;">BRENLOW</span>
      </div>
      <span class="brand__tagline" style="font-size:3.4px; margin-top:2px; margin-left:12px;">Development and Management Corp</span>
    </div>
    <p class="contact" style="left:8px; top:75px; font-size:3.8px;">123 Main Street, Any City, US 12345<br>+1 555 555 5555<br>email@company.com</p>
  </section>

</body>
</html>
```